T&R Custom Homes and Remodeling Flyer

We need a new double sided flyer that showcases our service.
Our website is http://trhomesbuildco.example/
Please use the information on http://trhomesbuildco.example/about-us/ for the information in the flyer.
This handout will be used to give to our potential customers and needs to show the complete story of who we are and the services we provide. I have also attached pictures of project we have completed that should be used for the flyer.
Any other pictures can be taken from our photo gallery on the website.

Target Market(s)

Clients who want a custom home or remodel

Industry/Entity Type

Construction

Font styles to use
Serif

Requirements
Must have
• Prominent logo
• Pictures of completed projects
• Tri-fold design- eps file is attached for this
Nice to have
• Manly colors
• If you can find a tasteful way to add the picture of the owners that is great, but it should be small and is not necessary.
Should not have
• Pink/girly touches

```html
<!DOCTYPE html>
<html lang="en">
<head>
<meta charset="utf-8">
<title>T&amp;R Custom Homes and Remodeling – Tri-fold Flyer</title>
<link rel="stylesheet" href="https://fonts.googleapis.com/css2?family=Source+Sans+3:wght@400;600&family=Parisienne&display=swap">
<style>
:root{
  --canvas:#e4e4e4;
  --charcoal:#3a3a3c;
  --paper:#f1f1f1;
  --teal:#3aa39b;
  --ink:#3a3a3a;
  --muted:#8a8a8a;
  --white:#ffffff;
}
*{box-sizing:border-box;margin:0;padding:0}
html,body{width:836px;height:1200px;overflow:hidden}
body{background:var(--canvas);font-family:"Source Sans 3",sans-serif;font-weight:400;color:var(--ink);position:relative}
.sheet{position:absolute;width:663px;height:513px;box-shadow:2px 3px 6px rgba(0,0,0,.25);overflow:hidden}
.sheet--outside{left:86px;top:64px;background:var(--paper)}
.sheet--inside{left:82px;top:631px;background:var(--charcoal)}
.abs{position:absolute}
.photo{position:absolute}
.panel-dark{background:var(--charcoal);color:var(--white)}
.heading{font-weight:400;color:var(--teal);font-size:12px}
.body-copy{font-size:7.6px;line-height:1.5;text-align:justify;font-weight:400}
.body-copy p+p{margin-top:8px}
.script{font-family:"Parisienne",cursive;color:var(--teal)}
.brand{font-weight:600;text-align:center;line-height:1.05}
.brand .sq{display:inline-block;width:9px;height:9px;background:currentColor;margin-bottom:3px}
.band{position:absolute;background:var(--teal);color:var(--white);text-align:center}
.testimonial{font-size:7.6px;line-height:1.48;color:#555;text-align:justify;font-weight:400}
.testimonial cite{display:block;font-style:normal;margin:9px 0 11px}
.contact{text-align:center;font-size:8.3px;line-height:1.5;color:#222;font-weight:400}
.contact h3{font-weight:400;color:var(--teal);font-size:10px;margin-bottom:8px}
.social{display:flex;gap:4px}
.social span{width:19px;height:19px;background:#9a9a9a;border-radius:2px}
.inside-copy{font-size:7.6px;line-height:1.5;text-align:justify;color:#333;font-weight:400}
</style>
</head>
<body>

<section class="sheet sheet--outside">
  <div class="abs panel-dark" style="left:0;top:0;width:220px;height:513px">
    <h2 class="heading abs" style="left:18px;top:24px">Our Mission</h2>
    <div class="body-copy abs" style="left:18px;top:44px;width:189px">
      <p>Over the years, we have developed close working relationships with some of the best local craftsmen, vendors, and suppliers located in the western suburbs of Chicago.</p>
      <p>These trade partners know we expect only the highest level of craftsmanship and they are required to perform at only the highest standards of professionalism, accuracy and timeliness. We take pride in creating homes that are as beautiful to look at, as they are comfortable to live in.</p>
    </div>
    <div class="photo" role="img" aria-label="Large brick custom home with a green lawn under a blue sky" style="left:0;top:173px;width:220px;height:167px;background:linear-gradient(180deg,#9ec0dd 0%,#c7d7e3 40%,#a48b74 58%,#6f8a3f 78%,#5c7d32 100%)"></div>
    <div class="script abs" style="left:14px;top:343px;font-size:17px">Where every detail matters</div>
    <div class="photo" role="img" aria-label="The two partners in company shirts" style="left:0;top:382px;width:131px;height:91px;background:linear-gradient(180deg,#d8cfc4,#b9ab9c 55%,#2b2b2b 75%)"></div>
    <div class="brand abs" style="left:136px;top:394px;width:78px;font-size:11px;color:var(--white)"><span class="sq"></span><br>T&amp;R<br><span style="font-size:6.5px">CUSTOM HOMES</span></div>
    <div class="abs" style="left:136px;top:432px;font-size:6.8px;line-height:1.6">Rick Dolan- Partner<br>Tom Harlan- Partner</div>
  </div>

  <div class="band" style="left:0;top:482px;width:438px;height:13px;font-size:10.5px;line-height:13px;padding-left:210px">www.trhomesbuildco.example</div>

  <div class="abs" style="left:234px;top:28px;width:190px">
    <div class="testimonial">
      <p>"Six months ago we finished our basement and having T&amp;R Custom Homes &amp; Remodeling complete the job was one of the best decisions we had made during that process. From the initial consultation to the final walk through, Tom listened to what we wanted, offered suggestions when we needed it and provided us with a professional insight that we could not have done without. Our basement is not just a finished basement but an addition to our existing living space."</p>
      <cite>- Sean &amp; Mara Porter, Plainfield IL</cite>
      <p>"Tom is highly professional in the way he operates his business and is a customer service champion! T&amp;R Custom Homes &amp; Remodeling built us a quality home and they kept their promise before and after the sale. They have been prompt and very accommodating in dealing with the various warranty issues that have arisen since we moved in. If we were to build another home in this area, T&amp;R would be the first builder we would call."</p>
      <cite>- Mark &amp; Cindy Hale, Plainfield IL</cite>
      <p>"We had our basement finished by T&amp;R Custom Homes &amp; Remodeling last year, and although they came highly recommended, the work that they did exceeded all our expectations. Not only was there an incredible attention to detail, but the courtesy and service we received was superior. The basement looks fabulous and we couldn't be happier."</p>
      <cite>- The Bauers, Naperville IL</cite>
    </div>
  </div>

  <div class="contact abs" style="left:234px;top:402px;width:190px">
    <h3>CONTACT US</h3>
    Tom Harlan: 708-555-0142<br>
    Rick Dolan: 630-555-0187<br>
    2150 Oakmont Road Suite 14<br>
    Millbrook, IL 60599
  </div>

  <div class="brand abs" style="left:447px;top:84px;width:100px;font-size:20px;color:var(--charcoal)"><span class="sq"></span><br>T&amp;R<br><span style="font-size:9px">CUSTOM HOMES</span><br><span style="font-size:5.5px;font-weight:400">AND REMODELING</span></div>
  <div class="script abs" style="left:440px;top:252px;width:105px;text-align:right;font-size:15px;line-height:1.55">Where<br>every detail<br>matters</div>
  <div class="abs" style="left:440px;top:362px;width:104px;text-align:right;font-size:9.6px;line-height:1.45;color:var(--muted)">T&amp;R Custom Homes &amp; Remodeling, LLC serving the Chicago suburban area</div>
  <div class="social abs" style="left:453px;top:478px" aria-label="Social links"><span></span><span></span><span></span></div>

  <div class="photo" role="img" aria-label="Arched wooden front entry door with a potted red plant on a brick step" style="left:556px;top:0;width:107px;height:513px;background:linear-gradient(180deg,#4a423a 0%,#c9cdd0 18%,#8b5a3c 45%,#5e2f1f 70%,#8a6a55 100%)"></div>
</section>

<section class="sheet sheet--inside">
  <div class="abs" style="left:0;top:0;width:224px;height:513px;background:var(--paper)">
    <h2 class="heading abs" style="left:9px;top:17px">About us</h2>
    <div class="inside-copy abs" style="left:9px;top:36px;width:207px">
      <p>With more than 20 years combined experience in construction, T&amp;R maintains the absolute highest levels of quality, material, workmanship, and service in each and every project we build.</p>
      <p>A reputation is only as great as the last referral and we understand that the future of our business relies upon satisfied customers.</p>
    </div>
    <div class="photo" role="img" aria-label="Brick two-storey custom home at dusk" style="left:0;top:118px;width:224px;height:115px;background:linear-gradient(180deg,#dfe4e8 0%,#c9cdd0 35%,#9a6a52 60%,#4f6b33 100%)"></div>
    <h2 class="heading abs" style="left:9px;top:249px">Quality, Reliability, Value</h2>
    <div class="inside-copy abs" style="left:9px;top:267px;width:207px">
      <p>We take the time to fully understand our customer's expectations. Customer service is more than just a trendy marketing theme, it is the underlying philosophy in everything we do and our home buyers reap the benefits of this philosophy.</p>
      <p>T&amp;R is committed to building quality homes with meticulous craftsmanship, custom designs, and thoughtful touches that add to the homeowners' quality of life.</p>
    </div>
    <div class="photo" role="img" aria-label="White trimmed archway opening onto a staircase and hardwood floor" style="left:0;top:369px;width:224px;height:112px;background:linear-gradient(180deg,#e9e6e1 0%,#d6cfc6 60%,#6b4328 100%)"></div>
  </div>

  <div class="photo" role="img" aria-label="Kitchen with dark cabinets, white island and pendant lights" style="left:224px;top:0;width:285px;height:188px;background:linear-gradient(180deg,#d7d2cc 0%,#3b2a22 45%,#e4ddd2 70%,#4a2e1f 100%)"></div>
  <div class="photo" role="img" aria-label="Wooden double entry door with leaded glass inside a brick arch" style="left:515px;top:0;width:149px;height:286px;background:linear-gradient(180deg,#6a5446 0%,#7a4a2b 35%,#5b3420 70%,#b9a58f 100%)"></div>
  <div class="photo" role="img" aria-label="Dining room with chandelier and wainscoting" style="left:224px;top:194px;width:140px;height:92px;background:linear-gradient(180deg,#5a4a3b 0%,#c9c2b5 55%,#5a3522 100%)"></div>
  <div class="photo" role="img" aria-label="Wooden staircase with iron balusters" style="left:370px;top:194px;width:139px;height:92px;background:linear-gradient(160deg,#e4e0da 0%,#8a5b3a 55%,#3a2418 100%)"></div>
  <div class="photo" role="img" aria-label="Bathroom vanity with dark cabinets and mirrors" style="left:224px;top:293px;width:140px;height:188px;background:linear-gradient(180deg,#e6ded2 0%,#3a2a22 45%,#2d1f19 80%,#8a6b52 100%)"></div>
  <div class="photo" role="img" aria-label="Kitchen with butcher-block island, bar stools and tiled backsplash" style="left:370px;top:293px;width:294px;height:188px;background:linear-gradient(180deg,#cfd2d4 0%,#2f2a28 40%,#8a4e2d 70%,#5a3322 100%)"></div>

  <div class="band" style="left:0;top:487px;width:663px;height:12px"></div>
  <div class="abs" style="left:0;top:499px;width:224px;height:14px;background:var(--paper)"></div>
</section>

</body>
</html>
```